SPARK - and the compass of quiet days

I´m writing a book about CHANGE and the skills leaders needs to embody the transformation from being amanager to become leaders.
The title of the book in Icelandic is the same as the name of the project (which I want to be used on the designes is:) HAFALDAN
(with the subtitle:) og listin að hlusta

Change is not controlled or managed – Leading effective change is an art form which is one of the big reasons for why 70% of changes within companies fail. The main reason however, is that managers are tasked with managing and directing them. The art form of change is to put it in the hands of leaders who possess the emotional intelligence that is needed – all their other advantages intact – to lead change all the way.

The big problem when it comes to change is that there are too many managers and too few leaders within companies – leaders who possess emotional intelligence which is the most important skill a leader embodies to empower change. A leader has what it takes to empower followership.

A manager tends to push and control, make decisions that he presupposes others to implement the way he expects. An emotionally competent leader leads by example and enhances followership on that journey because of the trust and respect he has earned.

In few words: SOFT SKILLS ARE THE NEW HARD SKILLS!

```html
<!DOCTYPE html>
<html lang="is">
<head>
<meta charset="utf-8">
<title>HAFALDAN – og listin að hlusta</title>
<link href="https://fonts.googleapis.com/css2?family=Open+Sans:wght@400;600;700;800&display=swap" rel="stylesheet">
<style>
  :root {
    --page-bg: #f1f1f1;
    --cover-top: #8c1f24;
    --cover-mid: #a8483a;
    --cover-bottom: #d69176;
    --title-white: #f7f4f2;
    --rule-light: rgba(255, 235, 228, 0.75);
    --author-maroon: #5e0f16;
    --body-text: #fbeee8;
    --photo-box: rgba(240, 210, 200, 0.7);
    --art-light: #f6d6cc;
    --art-mid: #d98d7a;
    --art-dark: #6b1a1f;
  }
  * { margin: 0; padding: 0; box-sizing: border-box; }
  html, body {
    width: 1200px; height: 800px; overflow: hidden;
    background: var(--page-bg);
    font-family: "Open Sans", Arial, sans-serif;
  }
  .spread {
    position: absolute; left: 50px; top: 120px;
    width: 1100px; height: 540px;
    display: flex; gap: 20px;
  }
  .cover {
    position: relative; width: 540px; height: 540px;
    background: linear-gradient(180deg, var(--cover-top) 0%, var(--cover-mid) 45%, var(--cover-bottom) 100%);
    overflow: hidden;
  }
  .cover-title {
    position: absolute; left: 0; right: 0;
    text-align: center; color: var(--title-white);
    font-weight: 800; letter-spacing: 1px; line-height: 1;
  }
  .subtitle-band {
    position: absolute; left: 50%; transform: translateX(-50%);
    border-top: 1px solid var(--rule-light);
    border-bottom: 1px solid var(--rule-light);
    text-align: center; color: var(--title-white); font-weight: 400;
  }
  /* Front */
  .front .cover-title { top: 52px; font-size: 86px; }
  .front .subtitle-band { top: 160px; width: 330px; font-size: 26px; padding: 4px 0 8px; }
  .cover-art {
    position: absolute; left: 110px; top: 225px; width: 320px; height: 255px;
    background: radial-gradient(ellipse at 55% 40%, var(--art-light) 0%, var(--art-mid) 45%, rgba(107,26,31,0.55) 80%, rgba(107,26,31,0) 100%);
    border-radius: 50% 50% 12px 12px;
  }
  .front .author-name {
    position: absolute; left: 0; right: 0; bottom: 28px;
    text-align: center; color: var(--author-maroon);
    font-size: 27px; font-weight: 700; letter-spacing: 1px;
  }
  /* Back */
  .back .cover-title { top: 48px; font-size: 62px; }
  .back .subtitle-band { top: 125px; width: 280px; font-size: 19px; padding: 3px 0 6px; }
  .blurb {
    position: absolute; left: 58px; top: 195px; width: 424px;
    color: var(--body-text); font-size: 12.6px; line-height: 1.55;
  }
  .back-rule {
    position: absolute; left: 200px; top: 395px; width: 282px;
    border-top: 1px solid var(--rule-light);
  }
  .author-photo {
    position: absolute; left: 58px; top: 430px; width: 90px; height: 110px;
    background: var(--photo-box);
  }
  .author-bio { position: absolute; left: 170px; top: 420px; width: 312px; }
  .author-bio .author-name {
    color: var(--author-maroon); font-size: 18px; font-weight: 700; letter-spacing: 0.5px;
    margin-bottom: 6px;
  }
  .author-bio p { color: var(--body-text); font-size: 12px; line-height: 1.5; }
</style>
</head>
<body>
  <main class="spread">
    <section class="cover back">
      <h2 class="cover-title">HAFALDAN</h2>
      <p class="subtitle-band">og listin að hlusta</p>
      <p class="blurb">Lorem ipsum dolor sit amet, consectetuer adipiscing elit, sed diam nonummy nibh euismod tincidunt ut laoreet dolore magna aliquam erat volutpat. Ut wisi enim ad minim veniam, quis nostrud exerci tation ullamcorper suscipit lobortis nisl ut aliquip. Duis autem vel eum iriure dolor in hendrerit in vulputate velit esse molestie consequat, vel illum dolore eu feugiat nulla facilisis at vero eros et accumsan et iusto odio dignissim qui blandit praesent luptatum zzril delenit augue duis dolore te feugait. Lorem ipsum dolor sit amet, cons ectetuer adipiscing elit. Duis autem vel eum iriure dolor in hendrerit.</p>
      <div class="back-rule"></div>
      <div class="author-photo" role="img" aria-label="Portrait photo of the author"></div>
      <div class="author-bio">
        <h3 class="author-name">ARNAR SVEINSSON</h3>
        <p>Lorem ipsum dolor sit amet, consectetuer adipiscing elit, sed diam nonummy nibh euismod tincidunt ut laoreet dolore magna. Ut wisi enim ad minim veniam, quis nostrud exerci tation ullamcorper suscipit lobortis nisl ut aliquip. Duis autem vel eum iriure dolor in.</p>
      </div>
    </section>

    <section class="cover front">
      <h1 class="cover-title">HAFALDAN</h1>
      <p class="subtitle-band">og listin að hlusta</p>
      <div class="cover-art" role="img" aria-label="Illustration of a glowing globe with orbit lines and a team of business people in silhouette around a meeting table"></div>
      <p class="author-name">ARNAR SVEINSSON</p>
    </section>
  </main>
</body>
</html>
```